HVAC company business card design

We need a business card design for a HVAC company. The design must look professional. Both sides will be used. The total data to be on the business card is
Name
Position
Email
Direct Phone/Moile Phone
Company Contacts /Address, Phone, Fax, web)
All data will be submit once the design is confirmed. For generic purposes use;
Emre Toksoy
Managing Director
+902324815263 (Mobile)
4712 Sokak No: 9 KBSE Yenikent IZMIR TURKEY
Tel: +902324815263 Fax : +902324815269
www.luvon.com.tr

Target Market(s)

HVAC

Industry/Entity Type

Business

Contact Information for Business Card

The total data to be on the business card is
Name
Position
Email
Direct Phone/Moile Phone
Emre Toksoy
Managing Director
+902324815263 (Mobile)
www.luvon.com.tr
The BC will use both sides of the card. The front will include the full logo and the details for the business card holder. The business card can be divided into vertical/horizontal or to a special shape. The common data like the company address/phone/fax should be indicated elsewehere. The back can contain some part or the whole logo and must contain the web address.

Font styles to use
Serif
Sans Serif

Colors
0355a3
cfdfed

Requirements
Should not have
• Please be careful with the fonts, it shouldnt be too small or too big and must not interfere with the logo fonts. If you need to use a curvy shape please do not use as the logo is already curvy or use the curves from the logo (if it looks good, otherwise forget it)
• We are not in favor of pictograms, only if they are perfect use them.

```html
<!DOCTYPE html>
<html lang="en">
<head>
<meta charset="utf-8">
<title>Luvon Business Card</title>
<link rel="stylesheet" href="https://fonts.googleapis.com/css2?family=Questrial&family=Quicksand:wght@300;500&display=swap">
<style>
  :root {
    --stage: #222222;
    --paper: #ffffff;
    --ink: #3d4660;
    --brand-blue: #3a6fcc;
    --brand-blue-light: #4a9ae8;
  }
  * { margin: 0; padding: 0; box-sizing: border-box; }
  html, body { width: 1200px; height: 1000px; overflow: hidden; background: var(--stage); }
  .stage { position: relative; width: 1200px; height: 1000px; }
  .card {
    position: absolute; left: 266px; width: 668px; height: 380px;
    background: var(--paper);
    box-shadow: 0 6px 18px rgba(0,0,0,0.45);
  }
  .card--front { top: 72px; }
  .card--back { top: 508px; }

  .brand { display: flex; align-items: center; gap: 14px; }
  .brand-dot { width: 52px; height: 52px; border-radius: 50%; background: linear-gradient(135deg, var(--brand-blue-light), var(--brand-blue)); }
  .brand-name { font-family: "Questrial", sans-serif; color: var(--ink); letter-spacing: 2px; }

  .card--front .brand { position: absolute; left: 50%; top: 50%; transform: translate(-50%, -50%); gap: 20px; }
  .card--front .brand-dot { width: 120px; height: 120px; }
  .card--front .brand-name { font-size: 52px; }

  .card--back .brand { position: absolute; left: 49px; top: 54px; }
  .card--back .brand-name { font-size: 38px; }

  .contact { position: absolute; left: 352px; font-family: "Quicksand", sans-serif; font-weight: 300; color: var(--ink); font-size: 20px; line-height: 26px; }
  .contact--address { top: 55px; }
  .contact--phones { top: 168px; left: 351px; }
  .contact--web { top: 300px; color: var(--brand-blue); }

  .holder { position: absolute; left: 59px; top: 262px; }
  .holder-name { font-family: "Questrial", sans-serif; font-size: 38px; color: var(--ink); line-height: 44px; }
  .holder-role { font-family: "Questrial", sans-serif; font-size: 21px; color: var(--brand-blue); line-height: 24px; }
</style>
</head>
<body>
<main class="stage">
  <section class="card card--front">
    <div class="brand">
      <span class="brand-dot"></span>
      <span class="brand-name">LUVON</span>
    </div>
  </section>

  <section class="card card--back">
    <div class="brand">
      <span class="brand-dot"></span>
      <span class="brand-name">LUVON</span>
    </div>

    <p class="contact contact--address">4712 Sokak No: 9 KBSE<br>&nbsp;Yenikent IZMIR TURKEY</p>
    <p class="contact contact--phones">+902324815263<br>Tel: +902324815263<br>Fax : +902324815269</p>
    <p class="contact contact--web">www.luvon.com.tr</p>

    <div class="holder">
      <p class="holder-name">Emre Toksoy</p>
      <p class="holder-role">Managing Director</p>
    </div>
  </section>
</main>
</body>
</html>
```